Medical device box for kits used for self testing purposes. Attractive simplistic design

Looking for a design that will go on a box that offer multiple range of medical testing ranging from hormones panel to diabetes and thyroid hormones. looking for something attractive and simple to go on a box 6 x 4.5 x 1 inches. attached are some examples from competitors. and our logo that be incorporated with the design.
Picture of the boxes have been attached, pick the color you think goes best with your design.

Target Market(s)

Patients and regular consumers

Industry/Entity Type

Medical

Requirements
Nice to have
• Simple design that is eye catching

```html
<!DOCTYPE html>
<html lang="en">
<head>
<meta charset="UTF-8">
<title>Medical Kits – Box Front Panel</title>
<link rel="stylesheet" href="https://fonts.googleapis.com/css2?family=Nunito:wght@400;600;700;800&display=swap">
<style>
  :root {
    --page-bg: #f4f4f4;
    --panel-white: #ffffff;
    --title-grey: #555555;
    --body-ink: #1d1d1f;
    --brand-navy: #151a3c;
    --brand-yellow: #fdd835;
    --pattern-orange: #fb8c00;
    --pattern-amber: #fbc02d;
    --pattern-yellow: #fdd835;
  }
  * { margin: 0; padding: 0; box-sizing: border-box; }
  html, body {
    width: 996px;
    height: 1200px;
    overflow: hidden;
    background: var(--page-bg);
    font-family: "Nunito", sans-serif;
  }
  .canvas {
    position: relative;
    width: 996px;
    height: 1200px;
  }
  .box-front {
    position: absolute;
    left: 48px;
    top: 262px;
    width: 900px;
    height: 675px;
    display: flex;
    background: var(--panel-white);
    box-shadow: 0 14px 60px rgba(0, 0, 0, 0.10);
  }
  .info-side {
    position: relative;
    width: 464px;
    height: 100%;
    padding: 98px 40px 0 62px;
  }
  .product-title {
    font-size: 60px;
    line-height: 1;
    color: var(--title-grey);
    letter-spacing: -0.5px;
  }
  .product-title .title-strong { font-weight: 700; }
  .product-title .title-light { font-weight: 400; }
  .product-tagline {
    margin-top: 40px;
    width: 330px;
    font-size: 22px;
    font-weight: 400;
    line-height: 1.38;
    color: var(--body-ink);
  }
  .brand-lockup {
    position: absolute;
    left: 62px;
    bottom: 70px;
    display: flex;
    align-items: center;
    gap: 12px;
  }
  .brand-dot {
    width: 34px;
    height: 34px;
    border-radius: 50%;
    background: var(--brand-yellow);
  }
  .brand-name {
    font-size: 38px;
    font-weight: 800;
    color: var(--brand-navy);
    line-height: 1;
  }
  .pattern-side {
    flex: 1;
    height: 100%;
    background: linear-gradient(150deg,
      var(--pattern-orange) 0%,
      var(--pattern-amber) 35%,
      var(--pattern-yellow) 55%,
      var(--pattern-amber) 75%,
      var(--pattern-orange) 100%);
  }
</style>
</head>
<body>
  <main class="canvas">
    <section class="box-front">
      <div class="info-side">
        <h1 class="product-title"><span class="title-strong">Medical</span> <span class="title-light">Kits</span></h1>
        <p class="product-tagline">Lorem ipsum dolor sit amet, consec</p>
        <div class="brand-lockup">
          <span class="brand-dot"></span>
          <span class="brand-name">Nuvia Health</span>
        </div>
      </div>
      <div class="pattern-side" role="img" aria-label="Geometric pattern of overlapping orange and yellow circles, rings and diagonal bands"></div>
    </section>
  </main>
</body>
</html>
```